E-learning Information & Community Website Needs a Makeover

I'm looking for a design makeover for my website "TavenNest.club". TavenNest's aim is to connect people to online learning through forums, information, guides & independent reviews. The site was launched in September 2014 using a forum software (Xenforo), but now needs a more polished and sophisticated look which communicates expertise and professionalism. I would like to see designs that use the current "TavenNest" blue (#0070c0). To visit the current website, go to http://www.tavennest.club/

Target Market(s)

People wishing to study online

Industry/Entity Type

Club

Number of Pages Required

4 page

Font styles to use
Sans Serif

Requirements
Must have
• A simple, clear and sophisticated lading page with links to the site's key features: discussion forums, Useful resources, Reviews, News etc, Articles. (See layout idea file attached)
• The main pages are the Landing Page, Discussion Forums, Resources & Reviews
• I would like to see designs that use the current "TavenNest" blue (#0070c0).
Nice to have
• Something uncluttered and easy to understand. The design should convey expertise in the field of online learning, giving users a sense of trust in the site's offerings.
• To give an idea of the sort of thing I'm after, take a look at brimvale.com website (screenshot attached)

```html
<!DOCTYPE html>
<html lang="en">
<head>
<meta charset="utf-8">
<title>TavenNest – Connecting people to online learning</title>
<link href="https://fonts.googleapis.com/css2?family=Cabin:ital,wght@0,400;0,500;0,600;1,400&display=swap" rel="stylesheet">
<style>
:root{
  --brand:#0070c0;
  --brand-light:#8fc6f2;
  --nav:#333333;
  --hero-top:#0e6ed0;
  --hero-bottom:#2a8ee0;
  --green:#8cc63f;
  --green-dark:#6fae22;
  --orange:#f47c55;
  --purple:#7b6fae;
  --pink:#e45570;
  --sky:#5bb8dc;
  --yellow:#f4c542;
  --ink:#555;
  --muted:#8a8a8a;
  --band:#ededed;
  --footer:#e4f2f3;
  --panel:#e6f3f4;
}
*{box-sizing:border-box;margin:0;padding:0}
html,body{width:1027px;height:1200px;overflow:hidden}
body{font-family:"Cabin",Arial,sans-serif;background:#fff;position:relative;color:var(--ink)}
.abs{position:absolute}

/* top navigation */
.topbar{left:0;top:0;width:1027px;height:46px;background:var(--nav)}
.brand{left:137px;top:8px;font-size:25px;color:var(--brand-light);font-weight:400}
.main-nav{left:276px;top:15px;display:flex;gap:17px;font-size:13px;color:#fff}
.account{left:801px;top:15px;font-size:13px;color:var(--brand-light)}
.account .sep{margin:0 8px;color:#888}
.signup-btn{left:845px;top:11px;width:54px;height:24px;background:var(--brand);border-radius:3px;color:#fff;font-size:12.5px;text-align:center;line-height:24px}

/* hero */
.hero{left:0;top:46px;width:1027px;height:382px;background:linear-gradient(180deg,var(--hero-top),var(--hero-bottom) 70%,#1c7ed8)}
.hero-social{left:832px;top:75px;display:flex;gap:4px}
.dot{width:11px;height:11px;border-radius:50%;background:#fff}
.hero-title{left:137px;top:112px;font-size:46px;line-height:50px;color:#fff;font-weight:400;letter-spacing:-.3px}
.cta{background:linear-gradient(180deg,#9cd24a,var(--green-dark));border-radius:18px;color:#fff;text-align:center;font-size:17px;box-shadow:0 2px 0 rgba(0,0,0,.12)}
.hero-cta{left:136px;top:280px;width:187px;height:33px;line-height:33px}
.hero-art{left:510px;top:118px;width:445px;height:272px;border-radius:40px;background:radial-gradient(ellipse at center,rgba(255,255,255,.35),rgba(255,255,255,.08) 70%)}

/* feature tiles */
.tile{width:86px;height:86px;top:405px}
.tile svg{display:block;margin:21px auto 0}
.tile-label{top:499px;width:120px;text-align:center;font-size:12.5px;color:#555}

/* partner band */
.partners-band{left:0;top:540px;width:1027px;height:103px;background:var(--band)}
.partners{left:135px;top:559px;width:761px;height:66px;background:#fff;box-shadow:0 1px 2px rgba(0,0,0,.1);display:flex;align-items:center;justify-content:center;gap:34px;font-size:15px;color:#9a9a9a}
.partner{display:flex;align-items:center;gap:6px}
.partner i{display:block;width:14px;height:14px;background:#bdbdbd;border-radius:50%}
.arrow{top:583px;font-size:20px;color:#ccc}

/* recent threads */
.th-head{top:656px;font-size:13px;color:var(--brand)}
.th-head.title{font-size:14px}
.thread{left:140px;width:550px;height:72px;border-bottom:1px solid #ddd}
.badge{left:0;top:3px;width:51px;height:51px;border-radius:50%;background:var(--brand);color:#fff;font-size:9.5px;text-align:center;padding-top:12px;line-height:11px}
.tag{left:8px;top:40px;width:34px;height:11px;font-size:8px;line-height:11px;text-align:center;color:var(--brand);background:var(--green);transform:rotate(-6deg)}
.tag.courses{background:var(--orange);color:#fff}
.th-title{left:69px;top:15px;font-size:12.5px;color:var(--brand)}
.th-meta{left:69px;top:34px;font-size:9.5px;color:var(--muted)}
.reply{left:328px;top:6px;width:41px;height:28px;background:var(--brand);color:#fff;font-size:11.5px;text-align:center;line-height:28px}
.reply-tail{left:352px;top:34px;width:0;height:0;border-left:9px solid transparent;border-top:8px solid var(--brand)}
.views{left:386px;top:7px}
.last{left:465px;top:8px;font-size:9.5px;color:var(--brand);line-height:11px}
.last span{color:var(--muted)}

/* sidebar */
.feed{left:708px;top:651px;width:187px;height:198px;background:var(--panel)}
.feed-head{left:10px;top:10px;display:flex;align-items:center;gap:7px;font-size:12px;color:var(--brand)}
.feed-head i{display:block;width:24px;height:24px;border-radius:50%;background:var(--brand)}
.feed-list{left:5px;top:42px;width:177px;height:150px;background:#fff}
.tweet{left:6px;width:168px;font-size:8px;line-height:9.5px;color:#444}
.tweet .av{position:absolute;left:0;top:0;width:28px;height:28px;background:#2f6da3}
.tweet .av.alt{background:#fff;border:1px solid #456}
.tweet .av.n{background:#1d5e6c}
.tweet .body{position:absolute;left:34px;top:0;width:134px}
.tweet b{font-weight:400;color:var(--brand);font-size:9px}
.tweet em{font-style:normal;color:#999}
.follow{left:708px;top:859px;width:187px;height:38px;background:var(--panel)}
.follow-label{left:12px;top:13px;font-size:12.5px;color:#2b5f86}
.follow-icons{left:88px;top:10px;display:flex;gap:3px}
.follow-icons i{display:block;width:17px;height:17px;background:#3c6ea6}
.share-title{left:719px;top:915px;font-size:11px;font-style:italic;color:#2b5f86}
.sh{font-size:8px;display:flex;align-items:center;gap:3px}
.sh .btn{background:#eef3f8;border:1px solid #c7d3e0;color:#345;padding:0 4px;height:12px;line-height:11px}
.sh .btn.dark{background:#3b5b9a;color:#fff;border-color:#3b5b9a}
.sh .btn.blue{background:#1678b8;color:#fff;border-color:#1678b8}
.sh .count{border:1px solid #ccc;padding:0 3px;height:12px;line-height:11px;color:#555}

/* more activities */
.more{left:443px;top:985px;width:149px;height:44px;border-radius:75px 75px 0 0;background:var(--brand);color:#fff;font-size:11.5px;text-align:center;padding-top:7px}

/* footer */
.footer{left:0;top:1007px;width:1027px;height:193px;background:var(--footer)}
.footer-tag{left:0;top:1034px;width:1027px;text-align:center;font-size:18px;font-style:italic;color:var(--brand)}
.footer-cta{left:422px;top:1064px;width:187px;height:33px;line-height:33px}
.footer-links{left:249px;top:1110px;width:532px;height:47px;background:#f4fafa}
.footer-links nav{position:absolute;left:35px;top:16px;display:flex;gap:15px;font-size:11px;color:var(--brand)}
.to-top{position:absolute;left:475px;top:15px;display:flex;align-items:center;gap:6px;font-size:10px;color:#555}
.to-top i{display:block;width:15px;height:15px;border-radius:50%;background:var(--brand)}
.copyright{left:282px;top:1172px;font-size:8.5px;color:var(--muted)}
.footer-social{left:527px;top:1172px;display:flex;gap:3px}
.footer-social i{display:block;width:12px;height:12px;border-radius:50%;background:#1d5a99}
.legal{left:666px;top:1172px;font-size:8.5px;color:var(--brand);display:flex;gap:9px}
</style>
</head>
<body>

<header class="abs topbar"></header>
<div class="abs brand">TavenNest</div>
<nav class="abs main-nav">
  <span>Home</span><span>Forums</span><span>Resources</span><span>Members</span><span>FAQ</span><span>Blog</span><span>TavenNest Español</span><span>Nest Scoop</span>
</nav>
<div class="abs account">Login<span class="sep">|</span></div>
<div class="abs signup-btn">Signup</div>

<section class="abs hero"></section>
<div class="abs hero-social"><i class="dot"></i><i class="dot"></i><i class="dot"></i><i class="dot"></i></div>
<h1 class="abs hero-title">At the heart of<br>connecting people to<br>online learning</h1>
<div class="abs cta hero-cta">Sign Up For Free</div>
<div class="abs hero-art" role="img" aria-label="Illustration of a classroom, a desktop screen showing the TavenNest name, devices, a settings gear and a graduation cap joined by a dashed loop"></div>

<!-- feature tiles -->
<div class="abs tile" style="left:179px;background:var(--green)">
  <svg width="44" height="44" viewBox="0 0 44 44"><circle cx="22" cy="22" r="17" fill="none" stroke="#fff" stroke-width="3"/><path d="M18 14l11 8-11 8z" fill="#fff"/></svg>
</div>
<div class="abs tile" style="left:295px;background:var(--orange)">
  <svg width="44" height="44" viewBox="0 0 44 44"><path d="M4 6h36v24H16l-7 7v-7H4z" fill="#fff"/><path d="M10 13h24M10 18h24M10 23h18" stroke="var(--orange)" stroke-width="2"/></svg>
</div>
<div class="abs tile" style="left:410px;background:var(--purple)">
  <svg width="44" height="44" viewBox="0 0 44 44"><path d="M5 5h34v26H20l-8 8v-8H5z" fill="#fff"/><circle cx="22" cy="18" r="8" fill="var(--purple)"/><path d="M18 18l3 3 5-6" stroke="#fff" stroke-width="2.2" fill="none"/></svg>
</div>
<div class="abs tile" style="left:526px;background:var(--pink)">
  <svg width="44" height="44" viewBox="0 0 44 44"><path d="M22 4a11 11 0 0 0-6 20v6h12v-6A11 11 0 0 0 22 4z" fill="none" stroke="#fff" stroke-width="2.2"/><path d="M17 34h10M18 38h8" stroke="#fff" stroke-width="2.2"/><path d="M20 29v-10l2 3 2-3v10" stroke="#fff" stroke-width="1.4" fill="none"/></svg>
</div>
<div class="abs tile" style="left:641px;background:var(--sky)">
  <svg width="44" height="44" viewBox="0 0 44 44"><path d="M9 3h19l9 9v30H9z" fill="#fff"/><path d="M28 3v9h9" fill="#d6eef7"/><path d="M14 20h18M14 25h18M14 30h18M14 35h14" stroke="var(--sky)" stroke-width="1.6"/></svg>
</div>
<div class="abs tile" style="left:758px;background:var(--yellow)">
  <svg width="44" height="44" viewBox="0 0 44 44"><rect x="3" y="9" width="38" height="26" fill="#fff"/><path d="M3 9l19 15 19-15" stroke="var(--yellow)" stroke-width="2" fill="none"/></svg>
</div>
<div class="abs tile-label" style="left:162px">Getting Started</div>
<div class="abs tile-label" style="left:278px">Discussions</div>
<div class="abs tile-label" style="left:393px">Reviews</div>
<div class="abs tile-label" style="left:509px">Tips &amp; Guidelines</div>
<div class="abs tile-label" style="left:624px">News &amp; Articles</div>
<div class="abs tile-label" style="left:741px">Newsletter</div>

<!-- partner strip -->
<section class="abs partners-band"></section>
<div class="abs partners">
  <span class="partner"><i></i>Paylumen</span>
  <span class="partner"><i></i>Cartwell</span>
  <span class="partner"><i></i>Ledra</span>
  <span class="partner">shopnook</span>
  <span class="partner"><i></i>Pagewright</span>
  <span class="partner"><i></i>STOCKRIVER</span>
</div>
<div class="abs arrow" style="left:140px">‹</div>
<div class="abs arrow" style="left:880px">›</div>

<!-- recent threads -->
<div class="abs th-head title" style="left:141px">Recent Threads</div>
<div class="abs th-head" style="left:470px">Replies</div>
<div class="abs th-head" style="left:534px">Views</div>
<div class="abs th-head" style="left:607px">Last Message</div>

<div class="abs thread" style="top:683px">
  <div class="abs badge">Taven<br>Nest</div><div class="abs tag">Advice</div>
  <div class="abs th-title">How many MOOCs have you done?</div>
  <div class="abs th-meta">Marisol, Sep 19, 2014, MOOC Discussions</div>
  <div class="abs reply">01</div><div class="abs reply-tail"></div>
  <svg class="abs views" width="42" height="26" viewBox="0 0 42 26"><path d="M1 13Q21-6 41 13Q21 32 1 13z" fill="var(--green)"/><circle cx="21" cy="13" r="9" fill="#fff"/><circle cx="21" cy="13" r="7.5" fill="var(--green-dark)"/><text x="21" y="17" font-size="10" fill="#fff" text-anchor="middle" font-family="Cabin,sans-serif">36</text></svg>
  <div class="abs last">Marisol,<br><span>Yesterday at 4:41 PM</span></div>
</div>
<div class="abs thread" style="top:755px">
  <div class="abs badge">Taven<br>Nest</div><div class="abs tag">Advice</div>
  <div class="abs th-title">How many MOOCs have you done?</div>
  <div class="abs th-meta">Marisol, Sep 19, 2014, MOOC Discussions</div>
  <div class="abs reply">01</div><div class="abs reply-tail"></div>
  <svg class="abs views" width="42" height="26" viewBox="0 0 42 26"><path d="M1 13Q21-6 41 13Q21 32 1 13z" fill="var(--green)"/><circle cx="21" cy="13" r="9" fill="#fff"/><circle cx="21" cy="13" r="7.5" fill="var(--green-dark)"/><text x="21" y="17" font-size="10" fill="#fff" text-anchor="middle" font-family="Cabin,sans-serif">36</text></svg>
  <div class="abs last">Marisol,<br><span>Yesterday at 4:41 PM</span></div>
</div>
<div class="abs thread" style="top:827px">
  <div class="abs badge">Taven<br>Nest</div><div class="abs tag courses">Courses</div>
  <div class="abs th-title">How many MOOCs have you done?</div>
  <div class="abs th-meta">Marisol, Sep 19, 2014, MOOC Discussions</div>
  <div class="abs reply">01</div><div class="abs reply-tail"></div>
  <svg class="abs views" width="42" height="26" viewBox="0 0 42 26"><path d="M1 13Q21-6 41 13Q21 32 1 13z" fill="var(--green)"/><circle cx="21" cy="13" r="9" fill="#fff"/><circle cx="21" cy="13" r="7.5" fill="var(--green-dark)"/><text x="21" y="17" font-size="10" fill="#fff" text-anchor="middle" font-family="Cabin,sans-serif">36</text></svg>
  <div class="abs last">Marisol,<br><span>Yesterday at 4:41 PM</span></div>
</div>
<div class="abs thread" style="top:904px;border-bottom:none">
  <div class="abs badge">Taven<br>Nest</div><div class="abs tag">Advice</div>
  <div class="abs th-title">How many MOOCs have you done?</div>
  <div class="abs th-meta">Marisol, Sep 19, 2014, MOOC Discussions</div>
  <div class="abs reply">01</div><div class="abs reply-tail"></div>
  <svg class="abs views" width="42" height="26" viewBox="0 0 42 26"><path d="M1 13Q21-6 41 13Q21 32 1 13z" fill="var(--green)"/><circle cx="21" cy="13" r="9" fill="#fff"/><circle cx="21" cy="13" r="7.5" fill="var(--green-dark)"/><text x="21" y="17" font-size="10" fill="#fff" text-anchor="middle" font-family="Cabin,sans-serif">36</text></svg>
  <div class="abs last">Marisol,<br><span>Yesterday at 4:41 PM</span></div>
</div>

<!-- sidebar -->
<aside class="abs feed">
  <div class="abs feed-head"><i></i>Chirp Feeds</div>
  <div class="abs feed-list">
    <div class="abs tweet" style="top:8px"><i class="av"></i><div class="body"><b>Brightloft</b> <em>@Brightloft 8/23/13</em><br>@danelwick is back with a blogpost on # API Interactions with #KVO in #Swiftly! - lnk.to/8k2mQ<br><em>Promoted by Brightloft</em></div></div>
    <div class="abs tweet" style="top:77px"><i class="av alt"></i><div class="body"><b>Brightloft</b> <em>@Brightloft</em><br>@danelwick is back with a blogpost on # API Interactions</div></div>
    <div class="abs tweet" style="top:116px"><i class="av n"></i><div class="body"><b>Brightloft</b> <em>@Brightloft</em><br>@danelwick is back with a blogpost on # API Interactions</div></div>
  </div>
</aside>
<div class="abs follow">
  <div class="abs follow-label">FOLLOW US</div>
  <div class="abs follow-icons"><i></i><i></i><i></i><i></i><i></i></div>
</div>
<div class="abs share-title">Share This Page</div>
<div class="abs sh" style="left:718px;top:938px"><span class="btn">Post</span><span class="count">139</span></div>
<div class="abs sh" style="left:803px;top:938px"><span class="btn">+1</span><span class="count">21</span></div>
<div class="abs sh" style="left:718px;top:955px"><span class="btn dark">Recommend</span><span class="count">157</span></div>
<div class="abs sh" style="left:803px;top:955px"><span class="btn blue">Share</span><span class="count">43</span></div>

<div class="abs more">⌄ more activities</div>

<!-- footer -->
<footer class="abs footer"></footer>
<div class="abs footer-tag">At the heart of connecting people to online learning</div>
<div class="abs cta footer-cta">Sign Up For Free</div>
<div class="abs footer-links">
  <nav><span>About</span><span>Contact Us</span><span>Help</span><span>Home</span><span>FAQ</span><span>Community Guidelines</span></nav>
  <div class="to-top"><i></i>Top</div>
</div>
<div class="abs copyright">All Rights Reserved ™ ©2010-2015 TavenNest.</div>
<div class="abs footer-social"><i></i><i></i><i></i><i></i></div>
<div class="abs legal"><span>Terms and Rules</span><span>Forum</span></div>

</body>
</html>
```